Want a package created for a new protein bar

We would like a new package created for a new protein bar project The name of the bar will be VOLMBite a real food protein bar, we would like a ‘window’ on the package of bar like Brave Meadow bar below in images.

VOLMBite
‘Super Food Bar’
14g of Whey Protein
The package film size is the following 12cm width x 15cm Length,
Flavor Peanut Chocolate Chip, additional information will be attached shortly like nutrition facts,

Target Market(s)

fitness market, bodybuilders, athletes, everyday people

Industry/Entity Type

Health Product

Logo Text

VOLMBite

Font styles to use
Serif
Sans Serif
Decorative

Requirements
Must have
• Package window

```html
<!DOCTYPE html>
<html lang="en">
<head>
<meta charset="utf-8">
<title>VOLMBite – Peanut Chocolate Chip wrapper</title>
<link rel="stylesheet" href="https://fonts.googleapis.com/css2?family=Archivo+Black&family=Alfa+Slab+One&family=Kalam:wght@400&family=Roboto+Condensed:wght@700&display=swap">
<style>
  :root {
    --backdrop: #8a8a8a;
    --film-light: #e3d2ad;
    --film-mid: #c9b07e;
    --film-dark: #9c8353;
    --panel-white: #e9e9ea;
    --window-grey: #b3b4b6;
    --window-line: #4dbb5a;
    --flavour-green: #2f963c;
    --brand-red: #7a1014;
    --ink: #141414;
    --paper: #ffffff;
  }
  * { box-sizing: border-box; margin: 0; padding: 0; }
  html, body { width: 1200px; height: 897px; overflow: hidden; }
  body { background: var(--backdrop); position: relative; font-family: "Roboto Condensed", sans-serif; }

  .wrapper { position: absolute; left: 0; top: 0; width: 1200px; height: 897px; }
  .wrapper-art { position: absolute; inset: 0; }

  .brand {
    position: absolute; left: 228px; top: 368px;
    font-family: "Archivo Black", sans-serif;
    font-size: 76px; line-height: 1; letter-spacing: -1px;
    color: var(--brand-red);
  }
  .tagline {
    position: absolute; left: 228px; top: 458px;
    font-family: "Kalam", cursive;
    font-size: 32px; letter-spacing: 2px; color: var(--ink);
  }
  .flavour { position: absolute; left: 835px; top: 352px; }
  .flavour-main {
    font-family: "Alfa Slab One", serif;
    font-size: 42px; line-height: 1; color: var(--ink);
  }
  .flavour-sub {
    font-family: "Alfa Slab One", serif;
    font-size: 21px; line-height: 1.2; color: var(--paper); margin-top: 2px;
  }
  .protein-badge {
    position: absolute; left: 870px; top: 433px; width: 88px;
    background: var(--paper); border-radius: 5px; overflow: hidden; text-align: center;
  }
  .protein-amount {
    background: var(--brand-red); color: var(--paper);
    font-family: "Archivo Black", sans-serif; font-size: 28px; line-height: 38px;
  }
  .protein-label { color: var(--ink); font-size: 14px; line-height: 22px; }
</style>
</head>
<body>
  <div class="wrapper">
    <svg class="wrapper-art" width="1200" height="897" viewBox="0 0 1200 897">
      <defs>
        <linearGradient id="film" x1="0" y1="0" x2="0" y2="1">
          <stop offset="0" stop-color="var(--film-light)"/>
          <stop offset="0.55" stop-color="var(--film-mid)"/>
          <stop offset="1" stop-color="var(--film-dark)"/>
        </linearGradient>
      </defs>
      <!-- film body with crimped seals -->
      <polygon class="film" fill="url(#film)"
        points="100,230 1100,230
                1112,248 1100,266 1112,284 1100,302 1112,320 1100,338 1112,356 1100,374 1112,392 1100,410
                1112,428 1100,446 1112,464 1100,482 1112,500 1100,518 1112,536 1100,554 1112,572 1100,590 1112,600
                100,600
                88,582 100,564 88,546 100,528 88,510 100,492 88,474 100,456 88,438 100,420
                88,402 100,384 88,366 100,348 88,330 100,312 88,294 100,276 88,258 100,240"/>
      <!-- flavour band -->
      <rect class="flavour-band" x="720" y="334" width="392" height="136" fill="var(--flavour-green)"/>
      <!-- brand panel -->
      <polygon class="brand-panel" fill="var(--panel-white)"
        points="88,300 585,300 700,418 585,536 88,536"/>
      <!-- window -->
      <polygon class="window" fill="var(--window-grey)" stroke="var(--window-line)" stroke-width="3"
        points="594,298 718,298 838,418 718,538 594,538 712,418"/>
    </svg>

    <div class="brand">VOLMBite</div>
    <div class="tagline">Super Food Bar</div>

    <div class="flavour">
      <div class="flavour-main">Peanut</div>
      <div class="flavour-sub">Chocolate Chip</div>
    </div>

    <div class="protein-badge">
      <div class="protein-amount">14g</div>
      <div class="protein-label">Whey Protein</div>
    </div>
  </div>
</body>
</html>
```